Property investment company needs a letterhead design!

We are a new residential and commercial property investment company. Name of the company is Morvessa Group, LLC. We have a new logo and now we need letterhead! We prefer to have a professional and upscale appearance. We don't have any fixed requirements, so be creative! Thank you for considering this project. We are so excited to see what happens!

Target Market(s)

Professional

Industry/Entity Type

Real Estate Development

```html
<!DOCTYPE html>
<html lang="en">
<head>
<meta charset="utf-8">
<title>Morvessa Group, LLC — Letterhead</title>
<link rel="stylesheet" href="https://fonts.googleapis.com/css2?family=Montserrat:wght@300;400;700;800&family=Fira+Sans+Condensed:wght@300;400&display=swap">
<style>
  :root {
    --navy: #061f3c;
    --sky: #0aaeea;
    --ink: #5a5a5a;
    --paper: #ffffff;
    --backdrop: #d6d6d6;
  }
  * { margin: 0; padding: 0; box-sizing: border-box; }
  html, body {
    width: 1056px; height: 1200px; overflow: hidden;
    background: var(--backdrop);
  }
  .letterhead {
    position: absolute; left: 118px; top: 20px;
    width: 820px; height: 1160px;
    background: var(--paper);
    overflow: hidden;
    color: var(--ink);
  }
  .brand {
    position: absolute; left: 78px; top: 118px;
    display: flex; align-items: center; gap: 10px;
    font-family: "Montserrat", sans-serif;
    font-weight: 800; font-size: 24px; letter-spacing: 0.5px;
    color: var(--navy);
  }
  .brand-dot {
    width: 34px; height: 34px; border-radius: 50%;
    background: var(--navy);
  }
  .contact {
    position: absolute; left: 578px; top: 70px;
    font-family: "Montserrat", sans-serif; font-size: 14.5px; font-style: normal;
    color: var(--ink); line-height: 18px;
  }
  .contact-lines { list-style: none; margin-top: 12px; }
  .contact-lines li { display: flex; align-items: center; gap: 14px; height: 21px; }
  .contact-lines svg { width: 15px; height: 15px; flex: none; }
  .date {
    position: absolute; left: 77px; top: 396px;
    font-family: "Montserrat", sans-serif; font-weight: 300; font-size: 18px;
  }
  .recipient-name {
    position: absolute; left: 77px; top: 426px;
    font-family: "Montserrat", sans-serif; font-weight: 700; font-size: 30px;
  }
  .recipient-role {
    position: absolute; left: 77px; top: 470px;
    font-family: "Montserrat", sans-serif; font-weight: 300; font-size: 18px;
  }
  .body {
    position: absolute; left: 77px; top: 540px; width: 665px;
    font-family: "Fira Sans Condensed", sans-serif; font-weight: 300;
    font-size: 15.6px; line-height: 28.5px;
    text-align: justify;
  }
  .body p + p { margin-top: 28.5px; }
  .body p.last { text-align: left; }
  .closing {
    position: absolute; left: 77px; top: 853px;
    font-family: "Fira Sans Condensed", sans-serif; font-weight: 300;
    font-size: 18px;
  }
  .signature {
    position: absolute; left: 78px; top: 900px;
    width: 85px; height: 59px;
    background: linear-gradient(135deg, #eef1f5, #dfe5ec);
  }
  .footer-band {
    position: absolute; left: 0; bottom: 0; width: 820px; height: 60px;
    background: linear-gradient(90deg, var(--navy), #0b3a66);
  }
</style>
</head>
<body>
<main class="letterhead">
  <div class="brand">
    <span class="brand-dot"></span>
    <span class="brand-name">Morvessa Group, LLC</span>
  </div>

  <address class="contact">
    <div>1234 First Line Address<br>5678 Second Line Address</div>
    <ul class="contact-lines">
      <li>
        <svg viewBox="0 0 16 16" aria-hidden="true"><path d="M3.5 1.5l2.5 0 1 3.5-1.6 1.2c.8 1.8 2.2 3.2 4 4l1.2-1.6 3.4 1v2.5c0 .8-.7 1.4-1.5 1.4C6.5 13.5 2.5 9.5 2.1 3c0-.8.6-1.5 1.4-1.5z" fill="var(--sky)"/><path d="M10 1.5a4.5 4.5 0 0 1 4.5 4.5M10 4a2 2 0 0 1 2 2" stroke="var(--sky)" stroke-width="1.3" fill="none"/></svg>
        +888 6666 9999
      </li>
      <li>
        <svg viewBox="0 0 16 16" aria-hidden="true"><rect x="1" y="3" width="14" height="10" fill="var(--sky)"/><path d="M1 3l7 5.5L15 3M1 13l5-4.5M15 13l-5-4.5" stroke="#fff" stroke-width="1.1" fill="none"/></svg>
        info@yourmail.com
      </li>
      <li>
        <svg viewBox="0 0 16 16" aria-hidden="true" fill="none" stroke="var(--sky)" stroke-width="1"><circle cx="8" cy="8" r="6.5"/><ellipse cx="8" cy="8" rx="3" ry="6.5"/><path d="M1.5 8h13M2.5 5h11M2.5 11h11"/></svg>
        www.yourwebsite.com
      </li>
    </ul>
  </address>

  <p class="date">10 December, 2021</p>
  <h1 class="recipient-name">DANIEL HARROW</h1>
  <p class="recipient-role">Cheif Executive Officer</p>

  <section class="body">
    <p>Contrary to popular belief, Lorem Ipsum is not simply random text. It has roots in a piece of classical Latin literature from 45 BC, making it over 2000 years old. Edwin Carrow, a Latin professor at Wrenfield College in Calder, looked up one of the more obscure Latin words, consectetur.</p>
    <p>Lorem Ipsum comes from sections 1.10.32 and 1.10.33 of "Liber Aequitatis Morum" (The Measure of Good and Evil) by Tavian Orle, written in 45 BC. This book is a treatise on the theory of ethics, very popular during the Renaissance. The first line of Lorem Ipsum.</p>
    <p class="last">The standard chunk of Lorem Ipsum used since the 1500s is reproduced below for those interested.</p>
  </section>

  <p class="closing">Best Regards</p>
  <div class="signature" role="img" aria-label="Handwritten signature"></div>

  <div class="footer-band" role="img" aria-label="Navy and blue decorative footer band"></div>
</main>
</body>
</html>
```